Maple Hollow Canine Massage Needs a Business Card Design

Maple Hollow Canine Massage is a new therapeutic canine massage company located in Nederland, Colorado. I need a business card design that include my logo and basic contact information.

Target Market(s)

Pet owners, veterinarians

Industry/Entity Type

Business

Contact Information for Business Card

Lydia Ferrow, CCMT
303.518.7269
lydia@maplehollowmassage.example
www.maplehollowmassage.example

Colors
6c459b
886aae
b8a6cd
a64599
b768aa
d3a5cc
fbed22

Requirements
Must have
• Font should be similar to font in logo.

```html
<!DOCTYPE html>
<html lang="en">
<head>
<meta charset="UTF-8">
<title>Maple Hollow Canine Massage – Business Card</title>
<link rel="stylesheet" href="https://fonts.googleapis.com/css2?family=Nunito:wght@400;700;800&display=swap">
<style>
  :root {
    --stage: #e9e6ea;
    --card-white: #fbf8fb;
    --violet-deep: #6c459b;
    --violet-mid: #886aae;
    --violet-soft: #b8a6cd;
    --magenta: #a64599;
    --magenta-mid: #b768aa;
    --magenta-soft: #d3a5cc;
    --gold: #c9a23a;
    --ink: #3b2d45;
    --name-ink: #8a3f86;
  }
  * { margin: 0; padding: 0; box-sizing: border-box; }
  html, body {
    width: 1200px;
    height: 970px;
    overflow: hidden;
    background: var(--stage);
  }
  .business-card {
    position: absolute;
    left: 80px;
    top: 182px;
    width: 1040px;
    height: 606px;
    background: var(--card-white);
    box-shadow: 0 18px 40px rgba(60, 40, 80, 0.18);
    font-family: "Nunito", sans-serif;
    overflow: hidden;
  }
  .card-bands {
    position: absolute;
    inset: 0;
    width: 100%;
    height: 100%;
  }
  .brand-mark {
    position: absolute;
    left: 646px;
    top: 60px;
    width: 300px;
    display: flex;
    flex-direction: column;
    align-items: center;
    gap: 18px;
  }
  .brand-dot {
    width: 150px;
    height: 150px;
    border-radius: 50%;
    background: var(--violet-deep);
  }
  .brand-name {
    font-weight: 800;
    font-size: 27px;
    line-height: 1.15;
    text-align: center;
    color: var(--violet-deep);
  }
  .holder-name {
    position: absolute;
    left: 66px;
    top: 320px;
    font-weight: 800;
    font-size: 37px;
    color: var(--name-ink);
  }
  .contact-list {
    position: absolute;
    left: 66px;
    top: 423px;
    list-style: none;
  }
  .contact-item {
    display: flex;
    align-items: center;
    height: 36px;
    font-size: 30px;
    font-weight: 400;
    color: var(--ink);
  }
  .contact-icon {
    width: 28px;
    height: 28px;
    margin-right: 18px;
    background: var(--gold);
    display: flex;
    align-items: center;
    justify-content: center;
  }
  .contact-icon svg { width: 18px; height: 18px; }
  .contact-web {
    margin-top: 10px;
    font-size: 27px;
    font-weight: 800;
    color: var(--name-ink);
  }
</style>
</head>
<body>
  <section class="business-card">
    <svg class="card-bands" viewBox="0 0 1040 606" preserveAspectRatio="none" aria-hidden="true">
      <defs>
        <linearGradient id="topBand" x1="0" y1="0" x2="1" y2="0">
          <stop offset="0" stop-color="#b768aa"/>
          <stop offset="0.5" stop-color="#a64599"/>
          <stop offset="1" stop-color="#886aae"/>
        </linearGradient>
        <linearGradient id="bottomBand" x1="0" y1="0" x2="1" y2="0">
          <stop offset="0" stop-color="#a64599"/>
          <stop offset="0.6" stop-color="#b768aa"/>
          <stop offset="1" stop-color="#886aae"/>
        </linearGradient>
      </defs>
      <path d="M0 0 H1040 V18 C760 20 300 110 0 268 Z" fill="url(#topBand)"/>
      <path d="M0 556 C360 560 780 470 1040 236 V606 H0 Z" fill="url(#bottomBand)"/>
    </svg>

    <div class="brand-mark">
      <div class="brand-dot"></div>
      <p class="brand-name">Maple Hollow<br>Canine Massage</p>
    </div>

    <h1 class="holder-name">Lydia Ferrow, CCMT</h1>

    <ul class="contact-list">
      <li class="contact-item">
        <span class="contact-icon">
          <svg viewBox="0 0 24 24"><path fill="#6c459b" d="M6.6 10.8a15.1 15.1 0 0 0 6.6 6.6l2.2-2.2c.3-.3.7-.4 1-.2 1.1.4 2.3.6 3.6.6.6 0 1 .4 1 1V20c0 .6-.4 1-1 1A17 17 0 0 1 3 4c0-.6.4-1 1-1h3.5c.6 0 1 .4 1 1 0 1.3.2 2.5.6 3.6.1.3 0 .7-.2 1z"/></svg>
        </span>
        303.518.7269
      </li>
      <li class="contact-item">
        <span class="contact-icon">
          <svg viewBox="0 0 24 24"><path fill="#6c459b" d="M3 5h18v14H3z"/><path fill="none" stroke="#c9a23a" stroke-width="1.8" d="M3 5l9 8 9-8"/></svg>
        </span>
        lydia@maplehollowmassage.example
      </li>
      <li class="contact-item contact-web">www.maplehollowmassage.example</li>
    </ul>
  </section>
</body>
</html>
```